依頼詳細
下記ブランドコンセプトに沿ったご提案をお願い致します。
プロトタイプを添付いたします。構成等、より優れていると思えるご提案がありましたら無視して頂いて構いません。
ブランドコンセプトは以下の通りです。

-- 以下、ブランドコンセプト
「自然が持つ美しさ」と「暮らす人の思い」を取り入れ『生活が楽しい住まい』を創ります
人々に永く愛されてきた天然素材を使用することで自然素材だけが持つ色や質感から確かな手触りと温もりを暮らす人に与え続けてくれます。新しいだけを追い過ぎず自然素材の持つ機能性を生かして自然の働きでしっかりと家を守る
それは流行に左右されない気品を保つ「素朴で美しい風合い」に仕上がります。

住む人のライフスタイルや好みをしっかりとお聞かせいただいた上で土地を生かし隣地環境と調和のある設計を企画し、その人らしい家を一緒に考えていきます。
それはその人がどんなふうに暮らしていきたいのかを一緒に考え、その地で永く暮らしていくイメージを膨らませ生活が楽しくなる様な空間を提案します。
-- 以上、ブランドコンセプト
サイトURL
http://morvatu.com/
ページ数
1ページ
希望イメージ
シンプル 複雑
単色 カラフル
暗い 明るい
日常 高級
遊び心 厳粛
未来的 伝統的
女性的 男性的
希望する色
納品ファイル
補足説明
トップページに関するプロトタイプを「トップページ.png」として添付しております。
また、素材として利用可能なものは下記dropboxリンクよりご利用ください。
https://www.filqeno-share.com/sh/7kdpqe31vmx02z/QWkrtyuu_pLmNnbvZxCdeRtYsUoPw?dl=0

■ 選んだ理由

全員が色使いやコンテンツの配置などを理由として同デザインを選択しました。
似通ったデザインの中でも全員の目を引く、魅力的な部分があったのだと考えます。

■ 提案者全員のお礼・コメント

今回は多くの皆様に貴重なお時間を使って頂きご提案頂きました事、大変うれしく思い感謝申し上げます。
複数名で選考を行いましたが、選考するメンバー全員でどれも素晴らしいデザインだよねと口をそろえて申しておりました。

本当にありがとうございました。

```html
<!DOCTYPE html>
<html lang="ja">
<head>
<meta charset="utf-8">
<title>Morvatu | 生活が楽しい住まい</title>
<link href="https://fonts.googleapis.com/css2?family=Noto+Sans+JP:wght@400;500;700&family=Noto+Serif+JP:wght@400;500&display=swap" rel="stylesheet">
<style>
:root{
  --olive:#b09d62;
  --olive-dark:#8e7c45;
  --ink:#3b3631;
  --text:#5a534c;
  --muted:#9a928a;
  --line:#e2ddd4;
  --band:#f1eee8;
  --paper:#ffffff;
  --footer:#3d3935;
  --photo-warm:#c9b79a;
  --photo-dark:#4a4036;
}
*{box-sizing:border-box;margin:0;padding:0}
html,body{width:711px;height:1200px;overflow:hidden;background:var(--paper)}
body{font-family:"Noto Sans JP",sans-serif;color:var(--text);font-size:9px;line-height:1.6;position:relative}
.topbar{height:16px;background:#f7f5f1;border-bottom:1px solid var(--line);display:flex;align-items:center;justify-content:space-between;padding:0 0 0 30px;font-size:7px;color:var(--muted)}
.topbar .contact-btn{background:var(--ink);color:#fff;height:16px;padding:0 22px;display:flex;align-items:center;margin-right:60px;font-size:7px}
.header{height:66px;display:flex;align-items:center;justify-content:space-between;padding:0 40px 0 64px}
.brand{display:flex;align-items:center;gap:8px}
.brand-mark{width:22px;height:22px;border:2px solid var(--olive)}
.brand-name{font-size:24px;font-weight:500;color:var(--ink);letter-spacing:.04em}
.header-tel{text-align:right}
.header-tel .note{font-size:8px;color:var(--text)}
.header-tel .num{display:flex;align-items:center;gap:6px;font-size:22px;font-weight:700;color:var(--olive);line-height:1.1}
.hero{position:relative;height:216px;background:var(--photo-dark)}
.hero-photo{position:absolute;left:52px;right:52px;top:0;bottom:0;background:linear-gradient(100deg,#8c7a63 0%,var(--photo-warm) 40%,#e6ddcc 65%,#a89579 100%)}
.hero-side{position:absolute;top:0;bottom:0;width:52px;background:linear-gradient(90deg,#2f2a25,#4c4339)}
.hero-side.right{right:0;background:linear-gradient(270deg,#2f2a25,#4c4339)}
.hero-copy{position:absolute;left:0;right:0;top:62px;text-align:center;color:#fff;font-family:"Noto Serif JP",serif}
.hero-copy h1{font-size:20px;font-weight:500;letter-spacing:.15em}
.hero-copy p{font-size:8px;letter-spacing:.05em;margin-top:2px}
.hero-arrow{position:absolute;top:98px;width:14px;height:22px}
.hero-dots{position:absolute;bottom:8px;left:0;right:0;display:flex;justify-content:center;gap:6px}
.hero-dots span{width:6px;height:6px;border-radius:50%;background:rgba(255,255,255,.5)}
.hero-dots span.on{background:#fff}
.nav{display:flex;margin:4px 0 0 0;padding-left:96px;height:36px;border-bottom:1px solid var(--line)}
.nav a{width:84px;display:flex;align-items:center;justify-content:center;font-size:8px;color:var(--text);text-decoration:none;border-left:1px solid var(--line)}
.nav a:first-child{background:var(--ink);color:#fff;border:none}
.nav a.current{background:var(--olive);color:#fff}
.section-label{font-size:8px;color:var(--olive-dark);letter-spacing:.08em;font-weight:500}
.concept{display:flex;padding:16px 24px 0 24px;gap:20px;height:195px}
.concept-text{flex:1}
.concept-text .section-label{border-bottom:1px solid var(--line);padding-bottom:4px;margin-bottom:10px}
.concept-text h2{font-family:"Noto Serif JP",serif;font-size:12px;font-weight:500;color:var(--ink);margin-bottom:8px}
.concept-text p{font-size:7px;line-height:1.9;color:var(--text);margin-bottom:6px}
.concept-photo{width:148px;height:144px;margin-top:14px;background:linear-gradient(160deg,#d9cdb8,#8f7c62 70%,#5d5044)}
.band{background:var(--band);height:470px;position:relative;padding:18px 24px}
.feature-tiles{display:flex;gap:8px;width:236px}
.tile{width:114px;height:72px;position:relative}
.tile.warm{background:var(--olive);color:#fff;display:flex;flex-direction:column;align-items:center;justify-content:center;font-size:8px;gap:4px}
.tile.warm .more{border:1px solid #fff;padding:1px 10px;font-size:6px}
.tile.photo{background:linear-gradient(135deg,#a79576,#dcd2bf)}
.info{position:absolute;left:24px;top:110px;width:400px}
.info-head{display:flex;justify-content:space-between;border-bottom:2px solid var(--olive);padding-bottom:4px;margin-bottom:4px}
.info-row{display:flex;align-items:center;gap:10px;height:18px;border-bottom:1px dotted var(--line);font-size:7px}
.info-row .date{color:var(--muted);width:46px}
.info-row .tag{background:var(--olive);color:#fff;font-size:6px;padding:0 5px;width:34px;text-align:center}
.btn{display:inline-block;background:var(--ink);color:#fff;font-size:7px;padding:3px 18px}
.info .btn{position:absolute;right:0;margin-top:8px}
.sns{position:absolute;left:24px;top:245px;width:400px;height:148px;background:var(--paper);border:1px solid var(--line)}
.sns-head{background:#f4f2ee;height:18px;padding:0 8px;font-size:7px;display:flex;align-items:center;border-bottom:1px solid var(--line)}
.sns-post{display:flex;gap:8px;padding:8px}
.sns-post .thumb{width:30px;height:30px;background:#cbbfa9}
.sns-post .title{font-size:8px;color:var(--ink);font-weight:500}
.sns-post .sub{font-size:7px;color:var(--muted)}
.sns-faces{display:grid;grid-template-columns:repeat(12,24px);gap:4px;padding:2px 8px}
.sns-faces span{height:24px;background:#d6ccbb}
.works{position:absolute;right:24px;top:0;width:210px;background:var(--paper);height:490px;padding:14px 10px;top:-8px}
.works-head{display:flex;justify-content:space-between;border-bottom:1px solid var(--line);padding-bottom:4px;margin-bottom:10px}
.work{display:flex;gap:8px;margin-bottom:14px}
.work .thumb{width:72px;height:50px;background:linear-gradient(135deg,#b7a587,#e3dac9)}
.work .meta{font-size:6.5px;line-height:1.7}
.work .meta b{color:var(--ink);font-weight:500;display:block}
.works .btn{float:right}
.pagetop{position:absolute;right:24px;top:1004px;background:var(--footer);color:#fff;font-size:7px;padding:2px 12px}
.footer{position:absolute;left:0;right:0;bottom:0;height:180px;background:var(--footer);color:#cfc8bf;padding:22px 40px}
.footer .brand-name{color:#fff;font-size:22px}
.footer .brand-mark{border-color:#fff}
.footer-nav{position:absolute;left:300px;top:40px;display:grid;grid-template-columns:repeat(6,auto);gap:4px 16px;font-size:7px}
.footer-nav .on{color:var(--olive)}
.footer-info{position:absolute;left:300px;top:76px;font-size:7px;line-height:1.9}
.copyright{position:absolute;left:40px;bottom:12px;font-size:6.5px;color:#8f887f}
</style>
</head>
<body>
<div class="topbar"><span>自然素材を生かした住まいづくり｜注文住宅と暮らしの提案</span><span class="contact-btn">お問い合わせ</span></div>

<header class="header">
  <div class="brand"><span class="brand-mark"></span><span class="brand-name">Morvatu</span></div>
  <div class="header-tel">
    <div class="note">ご相談・お問い合わせはこちらまで</div>
    <div class="num">
      <svg width="16" height="16" viewBox="0 0 24 24"><path fill="#b09d62" d="M6.6 10.8a15 15 0 0 0 6.6 6.6l2.2-2.2a1 1 0 0 1 1-.25 11.4 11.4 0 0 0 3.6.57 1 1 0 0 1 1 1V20a1 1 0 0 1-1 1A17 17 0 0 1 3 4a1 1 0 0 1 1-1h3.5a1 1 0 0 1 1 1c0 1.25.2 2.45.57 3.57a1 1 0 0 1-.25 1z"/></svg>
      0120-48-3917
    </div>
  </div>
</header>

<section class="hero">
  <div class="hero-side"></div>
  <div class="hero-photo" role="img" aria-label="自然光が差し込む木の床の明るいリビング"></div>
  <div class="hero-side right"></div>
  <div class="hero-copy"><h1>生活が楽しい住まい</h1><p>自然素材のぬくもりと暮らす人の思いをかたちにします</p></div>
  <svg class="hero-arrow" style="left:20px" viewBox="0 0 14 22"><path d="M11 2 3 11l8 9" stroke="#fff" stroke-width="2" fill="none"/></svg>
  <svg class="hero-arrow" style="right:20px" viewBox="0 0 14 22"><path d="m3 2 8 9-8 9" stroke="#fff" stroke-width="2" fill="none"/></svg>
  <div class="hero-dots"><span class="on"></span><span></span><span></span></div>
</section>

<nav class="nav">
  <a>HOME</a><a class="current">家づくり</a><a>建築事例</a><a>お問い合わせ</a><a>施工事例</a><a>会社概要</a>
</nav>

<section class="concept">
  <div class="concept-text">
    <div class="section-label">BRAND CONCEPT</div>
    <h2>ブランドコンセプト</h2>
    <p>「自然が持つ美しさ」と「暮らす人の思い」を取り入れ『生活が楽しい住まい』を創ります。人々に永く愛されてきた天然素材を使用することで、自然素材だけが持つ色や質感から確かな手触りと温もりを暮らす人に与え続けてくれます。</p>
    <p>新しいだけを追い過ぎず、自然素材の持つ機能性を生かして自然の働きでしっかりと家を守る。それは流行に左右されない気品を保つ「素朴で美しい風合い」に仕上がります。</p>
    <p>住む人のライフスタイルや好みをしっかりとお聞かせいただいた上で、土地を生かし隣地環境と調和のある設計を企画し、その人らしい家を一緒に考えていきます。</p>
  </div>
  <div class="concept-photo" role="img" aria-label="木の格子越しに見える室内の写真"></div>
</section>

<section class="band">
  <div class="feature-tiles">
    <div class="tile warm"><span>こだわりの家づくり</span><span class="more">MORE</span></div>
    <div class="tile photo" role="img" aria-label="無垢材の床と階段の写真"></div>
  </div>

  <div class="info">
    <div class="info-head"><span class="section-label">INFORMATION</span><span style="font-size:7px">お知らせ</span></div>
    <div class="info-row"><span class="date">2016.11.30</span><span class="tag">現場</span><span>「自然素材の住まい」完成見学会を開催いたします</span></div>
    <div class="info-row"><span class="date">2016.11.25</span><span class="tag">現場</span><span>「自然素材の住まい」完成見学会を開催いたします</span></div>
    <div class="info-row"><span class="date">2016.11.18</span><span class="tag">現場</span><span>「自然素材の住まい」完成見学会を開催いたします</span></div>
    <div class="info-row"><span class="date">2016.11.10</span><span class="tag">イベント</span><span>木の家づくり相談会のお知らせ</span></div>
    <div class="info-row"><span class="date">2016.11.02</span><span class="tag">イベント</span><span>木の家づくり相談会のお知らせ</span></div>
    <span class="btn">過去の一覧</span>
  </div>

  <div class="sns">
    <div class="sns-head">SNS ページ</div>
    <div class="sns-post">
      <div class="thumb"></div>
      <div><div class="title">Morvatu 自然素材の住まい</div><div class="sub">いいね！ 128件</div></div>
    </div>
    <div class="sns-faces"><span></span><span></span><span></span><span></span><span></span><span></span><span></span><span></span><span></span><span></span><span></span><span></span><span></span><span></span><span></span><span></span><span></span><span></span><span></span><span></span><span></span><span></span><span></span><span></span></div>
  </div>

  <aside class="works">
    <div class="works-head"><span class="section-label">施工事例</span><span style="font-size:7px">WORKS</span></div>
    <div class="work"><div class="thumb" role="img" aria-label="施工事例の住宅写真"></div><div class="meta"><b>木のぬくもりの家</b>自然素材を使った平屋の住まい</div></div>
    <div class="work"><div class="thumb" role="img" aria-label="施工事例の住宅写真"></div><div class="meta"><b>光と風の家</b>吹き抜けのある明るい住まい</div></div>
    <div class="work"><div class="thumb" role="img" aria-label="施工事例の住宅写真"></div><div class="meta"><b>庭とつながる家</b>土間と縁側のある住まい</div></div>
    <div class="work"><div class="thumb" role="img" aria-label="施工事例の住宅写真"></div><div class="meta"><b>素朴な風合いの家</b>漆喰と無垢材の住まい</div></div>
    <div class="work"><div class="thumb" role="img" aria-label="施工事例の住宅写真"></div><div class="meta"><b>家族が集う家</b>広いリビングの住まい</div></div>
    <div class="work"><div class="thumb" role="img" aria-label="施工事例の住宅写真"></div><div class="meta"><b>永く暮らす家</b>手入れしやすい住まい</div></div>
    <span class="btn">一覧を見る</span>
  </aside>
</section>

<span class="pagetop">PAGE TOP</span>

<footer class="footer">
  <div class="brand"><span class="brand-mark"></span><span class="brand-name">Morvatu</span></div>
  <div class="footer-nav"><span>HOME</span><span>家づくり</span><span>建築事例</span><span class="on">施工事例</span><span>会社概要</span><span>お問い合わせ</span></div>
  <div class="footer-info">〒000-0000 長野県山里市緑町1-2-3<br>TEL 0120-48-3917　営業時間 9:00〜18:00</div>
  <div class="copyright">Copyright (C) 2016 KALVENO All Rights Reserved.</div>
</footer>
</body>
</html>
```